Lanterns of the Silent Vale - Islamic Book about death, grave and the hereafter

We need a complete redesign of an old book cover. It is a book about death, the grave, the day of judgment, hellfire and paradise. i've attached our old bookcover. you can take new colors and change completly the design. It is up to you!

```html
<!DOCTYPE html>
<html lang="de">
<head>
<meta charset="utf-8">
<title>Lanterns of the Silent Vale – Buchumschlag</title>
<link rel="stylesheet" href="https://fonts.googleapis.com/css2?family=Tinos:wght@400;700&display=swap">
<style>
  :root {
    --stage: #000000;
    --gold-light: #fff3a8;
    --gold: #e9b821;
    --gold-deep: #a86a08;
    --brown: #7a4408;
    --spine-top: #e2a516;
    --spine-bottom: #9a5a0c;
    --band-yellow: #f7dd3a;
    --band-brown: #6b3a0a;
    --sky-top: #3f8fd6;
    --sky-mid: #bfe0f5;
    --haze: #f4f8fb;
    --mountain: #6f8aa0;
    --meadow: #7da23a;
    --meadow-deep: #4d6f24;
    --ink: #3a2206;
    --white: #ffffff;
  }
  * { margin: 0; padding: 0; box-sizing: border-box; }
  html, body { width: 1200px; height: 818px; overflow: hidden; background: var(--stage); }
  body { font-family: "Tinos", "Times New Roman", serif; position: relative; }

  .cover-spread { position: absolute; left: 80px; top: 50px; width: 1042px; height: 710px; }

  .back-cover {
    position: absolute; left: 0; top: 0; width: 481px; height: 710px;
    background:
      linear-gradient(180deg, rgba(240,200,60,0.95) 0%, rgba(232,190,60,0.85) 42%, rgba(190,170,60,0.55) 60%, rgba(120,140,50,0.6) 80%, rgba(140,150,60,0.7) 100%),
      linear-gradient(180deg, #f0c43a 0%, #b89a48 55%, #7c8f3a 100%);
  }

  .spine {
    position: absolute; left: 481px; top: 0; width: 80px; height: 710px;
    background: linear-gradient(180deg, var(--spine-top) 0%, #c7840f 50%, var(--spine-bottom) 100%);
  }
  .spine-title {
    position: absolute; left: 40px; top: 320px;
    transform: translate(-50%, -50%) rotate(-90deg);
    white-space: nowrap; font-size: 31px; color: var(--brown);
    line-height: 1;
  }
  .spine-title strong { font-weight: 400; letter-spacing: 0.5px; }
  .spine-imprint {
    position: absolute; left: 14px; top: 536px; width: 52px; height: 84px;
    background: var(--band-yellow);
    display: flex; flex-direction: column; align-items: center; justify-content: center; gap: 6px;
  }
  .spine-imprint .mark { width: 18px; height: 18px; background: var(--brown); }
  .spine-imprint .name { font-size: 7px; color: var(--brown); text-align: center; line-height: 1.1; }

  .front-cover {
    position: absolute; left: 561px; top: 0; width: 481px; height: 710px; overflow: hidden;
  }
  .front-photo {
    position: absolute; inset: 0;
    background:
      radial-gradient(ellipse 60% 30% at 30% 8%, rgba(255,255,255,0.9), rgba(255,255,255,0) 70%),
      linear-gradient(180deg, var(--sky-top) 0%, var(--sky-mid) 35%, var(--haze) 62%, var(--mountain) 70%, var(--meadow) 84%, var(--meadow-deep) 100%);
  }
  .author {
    position: absolute; left: 0; right: 0; top: 48px; text-align: center;
    font-size: 20px; font-weight: 700; letter-spacing: 0.3px;
    color: var(--gold);
    text-shadow: 0 1px 1px rgba(90,50,0,0.5);
  }
  .title { position: absolute; left: 0; right: 0; top: 185px; text-align: center; }
  .title-lead, .title-main {
    display: block; line-height: 1;
    background: linear-gradient(180deg, var(--gold-light) 0%, var(--gold) 45%, var(--gold-deep) 100%);
    -webkit-background-clip: text; background-clip: text; color: transparent;
    filter: drop-shadow(0 2px 1px rgba(80,40,0,0.45));
  }
  .title-lead { font-size: 44px; }
  .title-main { font-size: 98px; margin-top: 4px; letter-spacing: -1px; }
  .subtitle-band {
    position: absolute; left: 0; top: 340px; width: 481px; height: 32px;
    background: linear-gradient(90deg, var(--band-brown) 0%, #b5780f 45%, var(--band-yellow) 100%);
    color: var(--white); font-size: 26px; line-height: 32px; text-align: center;
  }
  .publisher {
    position: absolute; left: 0; right: 0; top: 652px; text-align: center;
    font-size: 17px; font-weight: 700; color: var(--ink);
  }
</style>
</head>
<body>
  <main class="cover-spread">
    <section class="back-cover" role="img" aria-label="Berglandschaft mit Schneefeldern unter goldenem Himmel"></section>

    <section class="spine">
      <div class="spine-title">Lanterns of the Silent <strong>VALE</strong></div>
      <div class="spine-imprint">
        <span class="mark"></span>
        <span class="name">Cedar Hall Press</span>
      </div>
    </section>

    <section class="front-cover">
      <div class="front-photo" role="img" aria-label="Sonniger Himmel über einem grünen Bergtal mit schneebedeckten Gipfeln"></div>
      <p class="author">MIRA HASSAN-OLUND</p>
      <h1 class="title">
        <span class="title-lead">Lanterns of the Silent</span>
        <span class="title-main">VALE</span>
      </h1>
      <p class="subtitle-band">Über den tod und das leben danach</p>
      <p class="publisher">Cedar Hall Press</p>
    </section>
  </main>
</body>
</html>
```